QLV Fashion Design Company Needs a New Web Design, Please Click Me

Designers:

PLEASE NOTE: we only need the web page design, not a fully coded website.

Our brand's name is The Bright Quarry, our signature is print. our style is edgy and chic.

The old website is too messy. here's the address:
www.qlvstudio.com.cn

The new website's purpose is to show our brand/design and most importantly, sell products, So it should be a combination of a designer official website and online shopping. I want the whole style to be clean, edgy and pioneer, easy to understand. we need a sophisticated online shopping website.

The reference websites are:
merolatest.co.uk
www.pd-kor.com
lucasvemm.com
orbaduvi.com
talumerosapkin.com

Please beat their designs :)

Check out our lasted fashion show to get to know us more.

https://www.vidplexa.com/watch?v=ZkamWtrBnoLe&spfreload=10

The attachments are our Logo and some 2015 Look Book.
(Please let us know if you want to play with our print in this particular web design, we can send the source file.)
Updates

Designers, we really like the design of ameliadrovenko.com(we have attached a picture of the website) , Can we get a homepage like that? so the designs you submit will be 3 pages. The first one should be a page that only has Shop/Look. then the shop page, it should be nothing but our product which we will list the categories ourself. And the look page should contain all the info. such as news, about us and designers etc. Thank you all for your hard work, we really enjoyed the designs. Added Monday, November 03, 2014

Target Market(s)

Our target audiences are woman aged from 16-40 who like online shopping

Industry/Entity Type

Online Shopping

Number of Pages Required

3 page

Font styles to use
Serif
Sans Serif
Script

Requirements
Must have
• Designers,
• we really like the design of ameliadrovenko.com(we have attached a picture of the website) , Can we get a homepage like that? so the designs you submit will be 3 pages. The first one should be a page that only has Shop/Look. then the shop page, it should be nothing but our product which we will list the categories ourself. And the look page should contain all the info. such as news, about us and designers etc. Thank you all for your hard work, we really enjoyed the designs.

```html
<!DOCTYPE html>
<html lang="en">
<head>
<meta charset="utf-8">
<title>QLV Group – The Bright Quarry</title>
<link rel="stylesheet" href="https://fonts.googleapis.com/css2?family=Cinzel:wght@400;500&family=Dosis:wght@300;400;500&display=swap">
<style>
  :root {
    --bg-dark: #2f2d2b;
    --bg-mid: #4a4744;
    --text-light: #f2f0ee;
    --line: rgba(255,255,255,0.28);
    --tile-light: #f3f1ef;
    --tile-mid: #d9d3ce;
    --ink: #111111;
    --accent: #b5121b;
    --field: rgba(190,188,186,0.55);
    --icon: #cfcdcb;
  }
  * { box-sizing: border-box; margin: 0; padding: 0; }
  html, body { width: 1200px; height: 750px; overflow: hidden; }
  body {
    font-family: "Dosis", sans-serif;
    color: var(--text-light);
    background: var(--bg-dark);
  }
  .page { position: relative; width: 1200px; height: 750px; overflow: hidden; }
  .hero-backdrop {
    position: absolute; inset: 0;
    background:
      radial-gradient(ellipse at 38% 35%, rgba(120,114,108,0.55), transparent 55%),
      linear-gradient(180deg, var(--bg-mid) 0%, #3b3936 45%, var(--bg-dark) 100%);
  }
  .menu-button {
    position: absolute; left: 171px; top: 35px; width: 97px; height: 33px;
    border: 1px solid rgba(255,255,255,0.8);
    display: flex; align-items: center; justify-content: center; gap: 10px;
    font-size: 13px; letter-spacing: 0.5px;
  }
  .menu-button svg { display: block; }
  .account-links {
    position: absolute; right: 171px; top: 43px;
    font-size: 13px; display: flex; gap: 18px;
  }
  .brand-mark {
    position: absolute; left: 527px; top: 34px; width: 146px; height: 146px;
    border-radius: 50%; background: #fff; border: 2px solid #8a8886;
    display: flex; align-items: center; justify-content: center;
    font-family: "Cinzel", serif; font-size: 34px; color: var(--accent);
  }
  .brand-title {
    position: absolute; left: 0; right: 0; top: 194px;
    text-align: center; font-family: "Cinzel", serif; font-weight: 400;
    line-height: 33px;
  }
  .brand-title .group { font-size: 31px; letter-spacing: 3px; display: block; }
  .brand-title .name { font-size: 31px; letter-spacing: 3px; display: block; }
  .gateway-tile {
    position: absolute; top: 303px; width: 423px; height: 203px;
    border: 1px solid #ffffff;
    display: flex; align-items: center; justify-content: center;
  }
  .gateway-tile.shop { left: 171px; background: linear-gradient(90deg, #e8e2dd 0%, var(--tile-light) 45%, #e6e2de 100%); }
  .gateway-tile.look { left: 607px; background: linear-gradient(90deg, #dcd6d2 0%, #efe3e3 40%, #ecdede 70%, #e2dbd6 100%); }
  .tile-label {
    width: 129px; padding: 8px 0 9px;
    border-top: 1px dotted #444; border-bottom: 1px dotted #444;
    text-align: center; font-size: 40px; font-weight: 400; color: var(--ink);
    line-height: 42px;
  }
  .info-block { position: absolute; top: 553px; width: 423px; }
  .info-block.social { left: 171px; }
  .info-block.newsletter { left: 606px; }
  .info-block h2 {
    border-top: 1px solid var(--line); border-bottom: 1px solid var(--line);
    height: 58px; line-height: 56px;
    font-size: 31px; font-weight: 300; letter-spacing: 0.3px;
  }
  .social-list { display: flex; gap: 13px; margin-top: 83px - 0; margin-top: 24px; list-style: none; }
  .social-list li {
    width: 37px; height: 37px; border-radius: 50%; background: var(--icon);
    color: #3a3836; font-size: 8px; font-weight: 500;
    display: flex; align-items: center; justify-content: center;
  }
  .signup-form { display: flex; gap: 5px; margin-top: 24px; }
  .email-field {
    width: 314px; height: 39px; background: var(--field);
    display: flex; align-items: center; justify-content: space-between;
    padding: 0 12px 0 15px; font-size: 12px; color: #f4f2f0;
  }
  .send-button {
    width: 107px; height: 39px; background: var(--accent);
    display: flex; align-items: center; justify-content: center;
    font-size: 13px; font-weight: 500;
  }
  .site-footer {
    position: absolute; left: 171px; top: 706px; width: 859px;
    border-top: 1px solid var(--line); text-align: center;
    padding-top: 13px; font-size: 12px;
  }
</style>
</head>
<body>
<div class="page">
  <div class="hero-backdrop" role="img" aria-label="Dimmed fashion photograph of a model seated on a rooftop above a city skyline"></div>

  <div class="menu-button">MENU
    <svg width="22" height="8" viewBox="0 0 22 8"><g stroke="#fff" stroke-width="1"><line x1="0" y1="0.5" x2="22" y2="0.5"/><line x1="0" y1="4" x2="22" y2="4"/><line x1="0" y1="7.5" x2="22" y2="7.5"/></g></svg>
  </div>

  <nav class="account-links"><span>LOGIN</span><span>/</span><span>SIGNUP</span></nav>

  <div class="brand-mark">QLV</div>
  <h1 class="brand-title"><span class="group">QLV GROUP</span><span class="name">THE BRIGHT QUARRY</span></h1>

  <a class="gateway-tile shop" role="img" aria-label="Studio photograph of two models in layered jackets">
    <span class="tile-label">SHOP</span>
  </a>
  <a class="gateway-tile look" role="img" aria-label="Photograph of friends walking with shopping bags">
    <span class="tile-label">LOOK</span>
  </a>

  <section class="info-block social">
    <h2>KEEP IN TOUCH</h2>
    <ul class="social-list">
      <li>Pixa</li><li>Chirpo</li><li>Plusly</li><li>Pinora</li><li>Vidplexa</li>
    </ul>
  </section>

  <section class="info-block newsletter">
    <h2>SIGNUP OUR NEWSLETTER</h2>
    <div class="signup-form">
      <div class="email-field">ENTER YOUR EMAIL HERE
        <svg width="24" height="18" viewBox="0 0 24 18"><g fill="none" stroke="#fff" stroke-width="1.2"><path d="M2 7 L18 2 L22 13 L6 17 Z"/><path d="M2 7 L13 11 L18 2"/><line x1="8" y1="16" x2="23" y2="16"/></g></svg>
      </div>
      <div class="send-button">SEND</div>
    </div>
  </section>

  <footer class="site-footer">Copyright @ 2014 The Bright Quarry All</footer>
</div>
</body>
</html>
```